Business Card

We need some ideas for corporate business cards. I'm interested in a double sided card, with one side featuring our corporate logo, the other side with employee information.

Corporate colors, logo etc. available at www.brivalo.com

Industry/Entity Type

Business

Requirements
Must have
• The "Brivalo" logo with stylized "O"

Nice to have
• Preferred font is calibri

```html
<!DOCTYPE html>
<html lang="en">
<head>
<meta charset="UTF-8">
<title>Brivalo Business Card</title>
<link rel="stylesheet" href="https://fonts.googleapis.com/css2?family=Carlito:wght@400;700&display=swap">
<style>
  :root {
    --brand-blue: #425a8a;
    --brand-blue-dark: #3a5080;
    --card-white: #ffffff;
    --card-grey: #d4d4d4;
    --ink: #333333;
    --backdrop-light: #ffffff;
    --backdrop-dark: #e2e2e2;
  }
  * { margin: 0; padding: 0; box-sizing: border-box; }
  html, body {
    width: 1200px;
    height: 1000px;
    overflow: hidden;
  }
  body {
    font-family: "Carlito", "Calibri", sans-serif;
    color: var(--ink);
    background: radial-gradient(ellipse at 50% 45%, var(--backdrop-light) 40%, var(--backdrop-dark) 100%);
    position: relative;
  }
  .card {
    position: absolute;
    box-shadow: 0 6px 14px rgba(0,0,0,0.22);
    overflow: hidden;
  }

  /* Front: logo side, portrait */
  .card-front {
    left: 116px;
    top: 211px;
    width: 330px;
    height: 578px;
    background: linear-gradient(to right, var(--card-white) 0%, #f1f1f1 55%, var(--card-grey) 100%);
  }
  .logo-block {
    position: absolute;
    left: 110px;
    top: 0;
    width: 190px;
    height: 262px;
    background: linear-gradient(to bottom, #4a64a0, var(--brand-blue-dark));
    display: flex;
    align-items: center;
    justify-content: center;
  }
  .logo-name {
    transform: rotate(-90deg);
    color: var(--card-white);
    font-weight: 700;
    font-size: 46px;
    letter-spacing: 5px;
    white-space: nowrap;
  }
  .web-block {
    position: absolute;
    left: 50px;
    top: 330px;
    width: 190px;
    height: 248px;
    background: var(--brand-blue-dark);
    display: flex;
    align-items: center;
    justify-content: center;
  }
  .web-address {
    transform: rotate(-90deg);
    color: var(--card-white);
    font-size: 17px;
    letter-spacing: 0.5px;
    white-space: nowrap;
  }

  /* Back: employee side, landscape */
  .card-back {
    left: 506px;
    top: 335px;
    width: 578px;
    height: 330px;
    background: linear-gradient(to bottom, #d9d9d9 0%, #ececec 55%, var(--card-white) 68%, var(--card-white) 100%);
  }
  .name-block {
    position: absolute;
    left: 0;
    top: 120px;
    width: 226px;
    height: 118px;
    background: var(--brand-blue);
    color: var(--card-white);
    padding: 38px 0 0 34px;
  }
  .person-name {
    font-weight: 700;
    font-size: 23px;
    line-height: 1.1;
  }
  .person-title {
    font-size: 15px;
    margin-top: 2px;
  }
  .contact-list {
    position: absolute;
    left: 252px;
    top: 78px;
    list-style: none;
    font-size: 14px;
    line-height: 20px;
  }
  .contact-label {
    color: var(--brand-blue);
    font-weight: 700;
  }
  .brand-square {
    position: absolute;
    left: 452px;
    top: 48px;
    width: 92px;
    height: 92px;
    background: var(--brand-blue);
  }
  .address-line {
    position: absolute;
    left: 34px;
    bottom: 30px;
    font-size: 17px;
  }
  .address-company {
    color: var(--brand-blue);
    font-weight: 700;
  }
</style>
</head>
<body>
  <section class="card card-front" aria-label="Card front">
    <div class="logo-block"><span class="logo-name">BRIVALO</span></div>
    <div class="web-block"><span class="web-address">www.brivalo.com</span></div>
  </section>

  <section class="card card-back" aria-label="Card back">
    <div class="name-block">
      <p class="person-name">Jane Doe</p>
      <p class="person-title">Chief Financial Officer</p>
    </div>
    <ul class="contact-list">
      <li><span class="contact-label">t:</span> +353 1 555 0140</li>
      <li><span class="contact-label">f:</span> +353 1 555 0190</li>
      <li><span class="contact-label">m:</span> +353 1 555 0140</li>
      <li><span class="contact-label">e:</span> info@brivalo.com</li>
    </ul>
    <div class="brand-square"></div>
    <p class="address-line"><span class="address-company">Brivalo,</span> 14 Harbour Lane, Riverside Business Park, Dublin 8</p>
  </section>
</body>
</html>
```